Gym Wall Story Feature-- Long Horizontal design for the full-width of the gym wall

We need a horizontal, LONG, story poster/display that artfully tells our gym's story using ALL of the attached information and photographs. I've also included where this display will go in our gym (aligned with, and under the trophies.) Please incorporate the color scheme of white, light grey, dark grey, and orange.

Thanks!

Target Market(s)

Upscale, exclusive, hip gym community

Industry/Entity Type

Gym

Font styles to use
Sans Serif

Colors
ffffff
000000
aaaaaa
5c5c5c
f78f20
e9e9e9

Requirements
Must have
• All images and text provided in the attachments. Clean, modern, design. MOSTLY white with just a couple pops of orange and light grey. text should be black or charcoal and easy to read. We would like to have our logo incorporated as well.
Nice to have
• Clean, stream-line look, nothing too busy or crowded.
Should not have
• Too busy, slanted lines, weird fonts, misalignment.

```html
<!DOCTYPE html>
<html lang="en">
<head>
<meta charset="utf-8">
<title>How Did The Method Start?</title>
<link href="https://fonts.googleapis.com/css2?family=Lato:wght@300;400;700&display=swap" rel="stylesheet">
<style>
  :root {
    --white: #ffffff;
    --black: #000000;
    --orange: #f78f20;
    --charcoal: #5c5c5c;
    --mid-grey: #aaaaaa;
    --light-grey: #e9e9e9;
    --photo-warm: #9a6a4a;
    --photo-mono: #3a3a3a;
    --photo-gym: #6b5a3e;
  }
  * { margin: 0; padding: 0; box-sizing: border-box; }
  html, body {
    width: 1200px; height: 724px; overflow: hidden;
    background: var(--white);
    font-family: "Lato", Arial, sans-serif;
  }
  .wall-story { position: relative; width: 1200px; height: 724px; }

  .headline {
    position: absolute; left: 66px; top: 104px;
    color: var(--orange); font-weight: 700;
    font-size: 57px; line-height: 61px; letter-spacing: 0.5px;
  }

  .quote-bubble { position: absolute; left: 464px; top: 188px; width: 174px; height: 110px; }
  .quote-bubble svg { position: absolute; left: 0; top: 0; }
  .quote-text {
    position: absolute; left: 0; top: 0; width: 172px; height: 66px;
    display: flex; align-items: center; justify-content: center; text-align: center;
    color: var(--white); font-weight: 300; font-size: 8.6px; line-height: 12px;
  }

  .photo {
    position: absolute; width: 94px; height: 149px;
    border: 1px solid var(--charcoal);
  }
  .photo--early { left: 123px; top: 305px; background: linear-gradient(160deg, #5a5a5a, var(--photo-mono) 60%, #1e1e1e); }
  .photo--stage { left: 443px; top: 305px; background: linear-gradient(170deg, #2a1a14, var(--photo-warm) 55%, #c7a27e); }
  .photo--today { left: 762px; top: 305px; background: linear-gradient(160deg, #b9a77a, var(--photo-gym) 50%, #1f1f1f); }

  .story-text {
    position: absolute; color: var(--charcoal);
    font-weight: 300; font-size: 8.6px; line-height: 11.2px;
  }
  .story-text p + p { margin-top: 10px; }
  .story-text .emphasis { font-weight: 400; color: #333; font-size: 8.8px; }
  .story-text--beginning { left: 233px; top: 304px; width: 186px; }
  .story-text--comeback { left: 572px; top: 301px; width: 156px; }
  .story-text--method { left: 872px; top: 305px; width: 186px; }

  .titles { position: absolute; left: 872px; top: 360px; width: 176px; }
  .titles-heading { color: var(--orange); font-weight: 700; font-size: 10.5px; letter-spacing: 0.2px; margin-bottom: 10px; }
  .title-row { display: flex; height: 15px; margin-bottom: 7px; font-size: 8.4px; color: var(--white); }
  .title-year { width: 27px; background: var(--orange); padding-left: 3px; line-height: 15px; }
  .title-name { flex: 1; background: var(--charcoal); line-height: 15px; padding-left: 27px; }

  .timeline { position: absolute; left: 0; top: 0; }
  .year {
    position: absolute; top: 508px; width: 80px; text-align: center;
    color: var(--orange); font-weight: 700; font-size: 18px;
  }
</style>
</head>
<body>
<main class="wall-story">
  <h1 class="headline">HOW DID<br>THE METHOD<br>START?</h1>

  <div class="quote-bubble">
    <svg width="174" height="110" viewBox="0 0 174 110" aria-hidden="true">
      <path d="M0 0 H172 V66 H50 L7 107 L20 66 H0 Z" fill="var(--orange)"/>
    </svg>
    <p class="quote-text">"I thought I was through and<br>couldn't continue lifting<br>but the method<br>changed everything."</p>
  </div>

  <svg class="timeline" width="1200" height="724" viewBox="0 0 1200 724" aria-hidden="true">
    <g stroke="var(--orange)" stroke-width="1">
      <line x1="67" y1="496" x2="181" y2="496"/>
      <line x1="378" y1="496" x2="428" y2="496"/>
      <line x1="445" y1="496" x2="498" y2="496"/>
      <line x1="693" y1="496" x2="747" y2="496"/>
      <line x1="765" y1="496" x2="827" y2="496"/>
      <line x1="1022" y1="496" x2="1126" y2="496"/>
      <polyline points="123,325 117,325 117,496" fill="none"/>
      <polyline points="443,325 437,325 437,496" fill="none"/>
      <polyline points="762,325 757,325 757,496" fill="none"/>
    </g>
    <g fill="var(--orange)">
      <circle cx="117" cy="496" r="6.5"/>
      <circle cx="437" cy="496" r="6.5"/>
      <circle cx="757" cy="496" r="6.5"/>
      <circle cx="1076" cy="496" r="6.5"/>
    </g>
    <g fill="#3c3c3c">
      <rect x="188" y="485" width="14" height="22" rx="3"/>
      <rect x="223" y="490" width="26" height="10" rx="3"/>
      <rect x="270" y="484" width="14" height="24" rx="2"/>
      <rect x="303" y="485" width="28" height="20" rx="3"/>
      <rect x="352" y="484" width="16" height="24" rx="3"/>
      <rect x="504" y="485" width="14" height="22" rx="3"/>
      <rect x="538" y="490" width="26" height="10" rx="3"/>
      <rect x="586" y="484" width="14" height="24" rx="2"/>
      <rect x="617" y="485" width="28" height="20" rx="3"/>
      <rect x="668" y="484" width="16" height="24" rx="3"/>
      <rect x="834" y="485" width="14" height="22" rx="3"/>
      <rect x="867" y="490" width="26" height="10" rx="3"/>
      <rect x="915" y="484" width="14" height="24" rx="2"/>
      <rect x="946" y="485" width="28" height="20" rx="3"/>
      <rect x="996" y="484" width="16" height="24" rx="3"/>
    </g>
  </svg>

  <span class="year" style="left:77px">1973</span>
  <span class="year" style="left:397px; top:505px">1981</span>
  <span class="year" style="left:717px; top:506px">2015</span>

  <div class="photo photo--early" role="img" aria-label="Black and white photo of a young Walden Price posing as a bodybuilder"></div>
  <div class="photo photo--stage" role="img" aria-label="Colour photo of Walden Price on stage at a bodybuilding competition"></div>
  <div class="photo photo--today" role="img" aria-label="Photo of Walden Price standing in the gym today"></div>

  <div class="story-text story-text--beginning">
    <p>The Method began with body builder and personal trainer, Walden Price. Walden had a passion for fitness early on and opened his first gym in 1960. Shortly after, Walden won Mr. Coastal State.</p>
    <p>Walden's body-building career looked promising until one evening he was robbed and shot in the chest. As a result, Walden suffered from nerve damage in the arm and figured at the age of 34, his weight lifting days were over.</p>
  </div>

  <div class="story-text story-text--comeback">
    <p>Walden started with 2-pound weights and changed his whole training technique. No more bouncing or slinging, just steady and controlled movements. Through hard work and consistency, Walden started shaping up his upper-body again.</p>
    <p class="emphasis">Shortly after turning 40, Walden won the National Mr. Continental competition.</p>
  </div>

  <div class="story-text story-text--method">
    <p>Through his experiences, Walden created The Method; a system that helps individuals develop a fundamentally sound workout regimen and accountability system.</p>
  </div>

  <section class="titles">
    <h2 class="titles-heading">NATIONAL CHAMPIONSHIPS WON:</h2>
    <div class="title-row"><span class="title-year">1981</span><span class="title-name">Won Past 40 Mr. Continental</span></div>
    <div class="title-row"><span class="title-year">1999</span><span class="title-name">Won Past 60 Mr. Continental</span></div>
    <div class="title-row"><span class="title-year">1996</span><span class="title-name">Won Past 50 Mr. Continental</span></div>
    <div class="title-row"><span class="title-year">2009</span><span class="title-name">Won Past 70 Mr. Continental</span></div>
  </section>
</main>
</body>
</html>
```